Copper Lantern LLC Business Card

We need a business card design for a newco in Texas. We are a team of professionals who join start ups as founders and help launch their businesses, which are primarily related to food and beverage and the service side of the industry. We love local and craft and are partners in businesses in the local meat, BBQ and Burger, fine dining, and beverage alcohol businesses. Our specialty is finance and the business side of start ups, including assisting with capital raises as principals, not brokers. We do not currently have any logos or graphics for this entity. Our values include helping people succeed, rooting for the underdog, healthy food, the environment and being good citizens.

Target Market(s)

Everybody but also Angel Investors, CPAs, Bankers, Entrepreneurs

Industry/Entity Type

Business

Contact Information for Business Card

Fields for Business Name, Title, Email Address, Phone Number. Place to add mailing address and web domain later.

Font styles to use
Sans Serif

Colors

Designer to choose colors to be used in the design.

Requirements
Should not have
• Pictures of booze bottles or drinks thought there could be a social scene that does not strictly focus on those. No cows, cowboy hats or ranches. We are not a Wall Street type entity so no huge office buildings or skylines.

```html
<!DOCTYPE html>
<html lang="en">
<head>
<meta charset="utf-8">
<title>Copper Lantern LLC Business Card</title>
<link href="https://fonts.googleapis.com/css2?family=Open+Sans:wght@400;600;700&display=swap" rel="stylesheet">
<style>
  :root {
    --amber: #d98e14;
    --amber-light: #e8a528;
    --amber-dark: #c47a0c;
    --paper: #f4f4f2;
    --ink: #3a3a3a;
    --ink-soft: #8a8a8a;
    --backdrop: #e9e6e1;
    --white: #ffffff;
  }
  * { box-sizing: border-box; margin: 0; padding: 0; }
  html, body { width: 1200px; height: 961px; overflow: hidden; }
  body {
    background: var(--backdrop);
    font-family: "Open Sans", Arial, sans-serif;
    position: relative;
  }
  .card {
    position: absolute;
    left: 290px;
    width: 620px;
    height: 354px;
    box-shadow: 0 6px 18px rgba(0,0,0,0.18);
    overflow: hidden;
  }
  /* Front */
  .card-front {
    top: 70px;
    background: linear-gradient(160deg, var(--amber-light) 0%, var(--amber) 55%, var(--amber-dark) 100%);
    color: var(--white);
    text-align: center;
  }
  .brand {
    position: absolute;
    top: 92px;
    left: 0; right: 0;
    display: flex;
    flex-direction: column;
    align-items: center;
  }
  .brand-mark {
    width: 34px; height: 34px;
    border-radius: 50%;
    background: var(--white);
    margin-bottom: 16px;
  }
  .brand-name { font-weight: 700; font-size: 30px; letter-spacing: 0.3px; }
  .brand-slogan { font-size: 9px; font-weight: 600; letter-spacing: 1px; margin-top: 4px; }
  .brand-rule {
    width: 250px; height: 1px; margin-top: 12px;
    background: linear-gradient(90deg, transparent, rgba(255,255,255,0.9), transparent);
  }
  .brand-web {
    margin-top: 36px; font-size: 19px; font-weight: 400;
    display: flex; align-items: center; gap: 8px;
  }
  /* Back */
  .card-back { top: 510px; background: var(--paper); color: var(--ink); }
  .back-art { position: absolute; inset: 0; }
  .contact {
    position: absolute;
    left: 40px;
    top: 106px;
    display: grid;
    grid-template-columns: 26px auto;
    column-gap: 22px;
    align-items: center;
  }
  .contact-icon { display: flex; justify-content: center; align-items: center; }
  .person-name { font-size: 17px; font-weight: 700; line-height: 22px; }
  .person-name span { font-weight: 400; color: var(--ink-soft); }
  .person-title { font-size: 9px; color: var(--ink-soft); line-height: 12px; }
  .contact-text { font-size: 14px; line-height: 17px; }
  .contact-text.strong { font-weight: 600; }
  .gap-sm { margin-top: 6px; }
  .gap-md { margin-top: 18px; }
  .gap-lg { margin-top: 12px; }
  .badge-text {
    position: absolute;
    left: 412px; top: 235px;
    width: 84px;
    text-align: center;
    color: var(--white);
  }
  .badge-text small { display: block; font-size: 8px; font-weight: 600; letter-spacing: 0.5px; }
  .badge-text strong { display: block; font-size: 14px; font-weight: 700; line-height: 18px; }
</style>
</head>
<body>

<section class="card card-front">
  <div class="brand">
    <div class="brand-mark"></div>
    <div class="brand-name">Copper Lantern LLC</div>
    <div class="brand-slogan">YOUR TAG SLOGAN</div>
    <div class="brand-rule"></div>
    <div class="brand-web">
      <svg width="14" height="14" viewBox="0 0 14 14"><circle cx="7" cy="7" r="6" fill="none" stroke="#fff" stroke-width="1.4"/><path d="M1 7h12M7 1c3 3 3 9 0 12M7 1c-3 3-3 9 0 12" fill="none" stroke="#fff" stroke-width="1"/></svg>
      copperlantern.co
    </div>
  </div>
</section>

<section class="card card-back">
  <svg class="back-art" width="620" height="354" viewBox="0 0 620 354">
    <defs>
      <linearGradient id="burgerTone" x1="0" y1="0" x2="1" y2="1">
        <stop offset="0" stop-color="#c98a4a"/><stop offset="0.5" stop-color="#8aa24a"/><stop offset="1" stop-color="#b2371f"/>
      </linearGradient>
      <radialGradient id="noodleTone"><stop offset="0" stop-color="#a9773f"/><stop offset="1" stop-color="#5a3f2a"/></radialGradient>
      <radialGradient id="curryTone"><stop offset="0" stop-color="#e07a3a"/><stop offset="1" stop-color="#b0481e"/></radialGradient>
    </defs>
    <path class="photo-burger" role="img" aria-label="Photo of a burger with lettuce, tomato and sauce" d="M330 0 H620 V175 Q560 120 470 95 Q390 75 330 0 Z" fill="url(#burgerTone)"/>
    <path d="M300 90 Q450 95 620 215" fill="none" stroke="var(--amber)" stroke-width="1.5"/>
    <circle cx="390" cy="150" r="80" fill="#fff"/>
    <circle cx="390" cy="150" r="80" fill="none" stroke="#e2e2e2" stroke-width="1"/>
    <circle cx="390" cy="150" r="68" fill="url(#noodleTone)" role="img" aria-label="Photo of a bowl of noodles"/>
    <circle cx="520" cy="190" r="64" fill="#fff"/>
    <circle cx="520" cy="190" r="64" fill="none" stroke="var(--amber)" stroke-width="1.5"/>
    <circle cx="520" cy="190" r="54" fill="url(#curryTone)" role="img" aria-label="Photo of a bowl of curry with cream swirl"/>
    <circle cx="454" cy="250" r="50" fill="#fff"/>
    <circle cx="454" cy="250" r="50" fill="none" stroke="#e2e2e2" stroke-width="1"/>
    <circle cx="454" cy="250" r="42" fill="var(--amber)"/>
    <rect x="0" y="340" width="620" height="14" fill="var(--amber)"/>
  </svg>

  <div class="contact">
    <div class="contact-icon">
      <svg width="22" height="24" viewBox="0 0 22 24"><circle cx="11" cy="7" r="5.5" fill="none" stroke="var(--amber)" stroke-width="1.8"/><path d="M1.5 23c0-5.5 4.3-9 9.5-9s9.5 3.5 9.5 9" fill="none" stroke="var(--amber)" stroke-width="1.8"/></svg>
    </div>
    <div>
      <div class="person-name">Your <span>Name</span></div>
      <div class="person-title">Designation</div>
    </div>

    <div class="contact-icon gap-sm">
      <svg width="22" height="16" viewBox="0 0 22 16"><path d="M2 5c0-3 18-3 18 0v2h-5V5H7v2H2z M4 8h14l2 7H2z" fill="var(--ink)"/><circle cx="11" cy="11" r="2" fill="var(--paper)"/></svg>
    </div>
    <div class="gap-sm">
      <div class="contact-text">000 .1234 .56789</div>
      <div class="contact-text">000 .1234 .5679</div>
    </div>

    <div class="contact-icon gap-md">
      <svg width="22" height="15" viewBox="0 0 22 15"><rect x="1" y="1" width="20" height="13" fill="var(--ink)"/><path d="M1 1l10 8 10-8" fill="none" stroke="var(--paper)" stroke-width="1.4"/></svg>
    </div>
    <div class="gap-md">
      <div class="contact-text">info@copperlantern.co</div>
      <div class="contact-text strong">www.copperlantern.co</div>
    </div>

    <div class="contact-icon gap-lg">
      <svg width="16" height="22" viewBox="0 0 16 22"><path d="M8 21C3 14 1 11 1 8a7 7 0 0 1 14 0c0 3-2 6-7 13z" fill="var(--ink)"/><circle cx="8" cy="8" r="2.5" fill="var(--paper)"/></svg>
    </div>
    <div class="gap-lg">
      <div class="contact-text">StreetAddressHere</div>
      <div class="contact-text">Country 2222</div>
    </div>
  </div>

  <div class="badge-text">
    <small>YOUR START-UP</small>
    <strong>PARTNER</strong>
  </div>
</section>

</body>
</html>
```